We sell companies excess stock for them

We need a business card for a company based in New Zealand called 'StockHarbor'.

Check out our website to get an idea www.stockharbor.example

We help other businesses to;
- Sell Excess Stock
- Manage Product Returns
- Sell Company Assets

Our logo is attached for your reference
The font used is 'RifficFree-Bold'

Target Market(s)

Businesses

Industry/Entity Type

Business

Contact Information for Business Card

Name: Mark Pellow
Phone: 027 846 2093
email: markpellow@stockharbor.example
website: www.stockharbor.example

Font styles to use
Other font styles liked:
• Unsure

Colors
9bcb3b

Requirements
Must have
• coming soon
Nice to have
• coming soon
Should not have
• coming soon

```html
<!DOCTYPE html>
<html lang="en">
<head>
<meta charset="UTF-8">
<title>StockHarbor Business Card</title>
<link href="https://fonts.googleapis.com/css2?family=Fredoka:wght@600;700&display=swap" rel="stylesheet">
<style>
  :root {
    --brand-green: #9bcb3b;
    --card-dark: #3a3634;
    --ink-dark: #2f2c2a;
    --white: #ffffff;
    --stage: #e9e9e7;
    --mascot-green: #7dbb35;
    --mascot-orange: #f0a532;
  }
  * { margin: 0; padding: 0; box-sizing: border-box; }
  html, body {
    width: 1200px; height: 900px; overflow: hidden;
    background: var(--stage);
    font-family: "Fredoka", sans-serif;
  }
  .canvas {
    width: 1200px; height: 900px;
    display: flex; flex-direction: column;
    align-items: center; justify-content: center; gap: 56px;
  }
  .card {
    width: 600px; height: 343px;
    position: relative; overflow: hidden;
    border-radius: 4px;
    box-shadow: 0 10px 28px rgba(0,0,0,0.18);
  }
  .card-front {
    background: var(--brand-green);
    display: flex; align-items: center; justify-content: center;
  }
  .brand-name {
    font-weight: 700; font-size: 64px; letter-spacing: -1px;
    color: var(--ink-dark);
  }
  .card-back { background: var(--card-dark); }
  .mascot {
    position: absolute; right: 0; top: 0;
    width: 290px; height: 250px;
    border-bottom-left-radius: 140px;
    background: linear-gradient(135deg, var(--mascot-green) 0%, #a6d25a 55%, var(--mascot-orange) 100%);
  }
  .holder {
    position: absolute; left: 40px; bottom: 34px;
  }
  .holder-name {
    font-weight: 700; font-size: 54px; line-height: 1; letter-spacing: -1px;
    margin-bottom: 14px;
  }
  .holder-first { color: var(--white); }
  .holder-last { color: var(--brand-green); }
  .contact-list { list-style: none; }
  .contact-item {
    display: flex; align-items: center; gap: 10px;
    color: var(--white); font-weight: 600; font-size: 18px; line-height: 1.45;
  }
  .contact-icon { width: 16px; height: 16px; flex: none; }
</style>
</head>
<body>
<main class="canvas">
  <section class="card card-front">
    <h1 class="brand-name">StockHarbor</h1>
  </section>

  <section class="card card-back">
    <div class="mascot" role="img" aria-label="Cartoon delivery mascot in a green cap giving a thumbs up and carrying an orange parcel"></div>
    <div class="holder">
      <h2 class="holder-name"><span class="holder-first">Mark</span><span class="holder-last">Pellow</span></h2>
      <ul class="contact-list">
        <li class="contact-item">
          <svg class="contact-icon" viewBox="0 0 16 16"><rect x="1" y="3" width="14" height="10" rx="1.5" fill="#9bcb3b"/><path d="M1.5 4l6.5 5 6.5-5" stroke="#3a3634" stroke-width="1.5" fill="none"/></svg>
          markpellow@stockharbor.example
        </li>
        <li class="contact-item">
          <svg class="contact-icon" viewBox="0 0 16 16"><circle cx="8" cy="8" r="7" fill="#9bcb3b"/><path d="M1 8h14M8 1c-3 3.5-3 10.5 0 14M8 1c3 3.5 3 10.5 0 14" stroke="#3a3634" stroke-width="1.2" fill="none"/></svg>
          www.stockharbor.example
        </li>
        <li class="contact-item">
          <svg class="contact-icon" viewBox="0 0 16 16"><path d="M4 1.5l2.5 3-1.5 2c1 2 2.5 3.5 4.5 4.5l2-1.5 3 2.5-1.5 2.5C7.5 16 0 8.5 1.5 3z" fill="#9bcb3b"/></svg>
          027 846 2093
        </li>
      </ul>
    </div>
  </section>
</main>
</body>
</html>
```